A Freight forwarding (transportation/shipping) company requires stationary design

We need The following:
1. Letterhead
2. Letter Envelope
3. A4 Paper Envelope
4. A4 Paper Folder (One that is 2xA4 foldable size which we can open in half and we can put a paper in between)
5. A5 Paper (To be used for notes taking)

a design for a freight forwarding company named BORUMAND TALAJ INTERNATIONAL TRANSPORTATION CO . Business Card is already designed and should follow it, the files attached help guide you in type of docs required + Logos (We are active in Sea Transportation, Truck transportation, and Air Transportation, (printed design is required with all open source files for editing - lamination accepted)

The said company is agent and sales representative of 2 other Shipping companies (whose logos, name, and website should also be mentioned on Envelopes and Folder) - Velor Tide and QMD Shipping, logos attached.

Velor Tide Shipping LLC
Dubai, United Arab Emirates
www.vtduae-example.com

QMD Shipping Line Ltd
London, United Kingdom
www.qmdfleet-example.com

Address is "No.8, 2nd Sadaf Kuy-e-Nilufari, Tehran, IR
Tel number is +98 21 55402913
Fax number is +98 21 55406287
E-Mail address is info@borumandtalaj-example.com
Website is www.borumandtalaj-example.com

```html
<!DOCTYPE html>
<html lang="en">
<head>
<meta charset="utf-8">
<title>Borumand Talaj – Presentation Folder</title>
<link rel="stylesheet" href="https://fonts.googleapis.com/css2?family=Montserrat:wght@400;600;700&family=Lora:wght@400&display=swap">
<style>
  :root{
    --bg:#d6d7d9;
    --paper:#f6f7f8;
    --sheet:#ffffff;
    --navy:#0c3a5d;
    --navy-line:#0a2f4c;
    --brand:#1f4f8a;
    --ink:#24406a;
    --muted:#5b6675;
    --white:#ffffff;
  }
  *{box-sizing:border-box;margin:0;padding:0}
  html,body{width:1200px;height:800px;overflow:hidden}
  body{background:var(--bg);font-family:"Montserrat",Arial,sans-serif;position:relative}

  .folder{position:absolute;left:80px;top:40px;width:1040px;height:720px;display:flex;box-shadow:0 10px 30px rgba(0,0,0,.18)}
  .panel{position:relative;width:520px;height:720px;background:var(--paper);overflow:hidden}
  .panel--left{background:linear-gradient(to right,var(--paper) 92%,#e6e8eb 100%)}
  .panel--right{background:linear-gradient(to left,var(--paper) 92%,#e6e8eb 100%)}

  .pocket{position:absolute;left:0;right:0;bottom:0;background:var(--navy);border-top:1px solid var(--navy-line)}
  .panel--left .pocket{height:330px}
  .panel--right .pocket{height:350px}

  /* letterhead */
  .letter{position:absolute;left:20px;top:16px;width:480px;height:680px;background:var(--sheet);padding:26px 30px;box-shadow:0 1px 4px rgba(0,0,0,.08)}
  .letter__head{display:flex;justify-content:space-between;align-items:flex-start;margin-bottom:30px}
  .brand{display:flex;align-items:center;gap:8px}
  .brand__dot{width:30px;height:30px;border-radius:50%;border:2px solid var(--brand)}
  .brand__name{font-weight:700;font-size:8px;line-height:1.25;color:var(--brand);letter-spacing:.2px}
  .contact{list-style:none;font-size:6.5px;line-height:1.5;color:var(--muted)}
  .contact li{display:flex;align-items:center;gap:4px}
  .contact svg{width:6px;height:6px;fill:var(--brand);flex:none}
  .greeting{font-family:"Lora",Georgia,serif;font-size:17px;color:var(--ink);margin-bottom:8px}
  .body p{font-size:7.5px;line-height:1.5;color:var(--muted);margin-bottom:12px}

  /* partners */
  .partners{position:absolute;left:0;right:0;bottom:0;height:330px;display:flex;justify-content:space-around;align-items:center;padding:0 30px}
  .partner{display:flex;flex-direction:column;align-items:center;gap:6px;color:var(--white);text-align:center}
  .partner__mark{display:flex;align-items:center;gap:8px}
  .partner__dot{width:26px;height:26px;border-radius:50%;background:var(--white)}
  .partner__name{font-weight:700;font-size:15px;letter-spacing:.3px}
  .partner__city,.partner__web{font-size:11px;letter-spacing:1px}

  /* card slot */
  .slot{position:absolute;left:120px;top:40px;width:280px;height:150px}
  .slot__cut{position:absolute;width:34px;height:1.5px;background:#061e33;top:-2px}
  .slot__cut--l{left:-14px;transform:rotate(-42deg);transform-origin:right center}
  .slot__cut--r{right:-14px;transform:rotate(42deg);transform-origin:left center}
  .card{position:absolute;inset:0;background:var(--sheet);padding:16px 16px 12px;display:flex;flex-direction:column;justify-content:space-between;box-shadow:0 2px 6px rgba(0,0,0,.25)}
  .card__top{display:flex;justify-content:space-between;align-items:flex-start}
  .card .brand__dot{width:22px;height:22px}
  .card .brand__name{font-size:6.5px;font-weight:700;text-transform:none}
  .person{text-align:right}
  .person__name{font-size:8px;font-weight:700;color:var(--ink);letter-spacing:.3px}
  .person__role{font-size:5.5px;color:var(--muted);margin-top:2px}
  .card__bottom{display:flex;justify-content:space-between;align-items:flex-end}
  .card .contact{font-size:5.5px}
  .card__addr{font-size:5.5px;color:var(--muted);text-align:right;line-height:1.5}
</style>
</head>
<body>
<main class="folder">
  <section class="panel panel--left">
    <article class="letter">
      <header class="letter__head">
        <div class="brand">
          <span class="brand__dot"></span>
          <p class="brand__name">BORUMAND TALAJ<br>INTERNATIONAL<br>TRANSPORTATION CO</p>
        </div>
        <ul class="contact">
          <li><svg viewBox="0 0 10 10"><path d="M2 1h2l1 2-1 1a6 6 0 0 0 2 2l1-1 2 1v2c0 .6-.4 1-1 1A8 8 0 0 1 1 2c0-.6.4-1 1-1z"/></svg>+98 21 55402913</li>
          <li><svg viewBox="0 0 10 10"><rect x="1" y="3" width="8" height="5"/><rect x="3" y="1" width="4" height="2"/></svg>+98 21 55406287</li>
          <li><svg viewBox="0 0 10 10"><path d="M1 2h8v6H1z M1 2l4 3 4-3"/></svg>info@borumandtalaj-example.com</li>
          <li><svg viewBox="0 0 10 10"><circle cx="5" cy="5" r="4"/></svg>www.borumandtalaj-example.com</li>
          <li><svg viewBox="0 0 10 10"><path d="M5 0a3.5 3.5 0 0 1 3.5 3.5C8.5 6 5 10 5 10S1.5 6 1.5 3.5A3.5 3.5 0 0 1 5 0z"/></svg>No.8, 2nd Sadaf Kuy-e-Nilufari,<br>Tehran, IRAN</li>
        </ul>
      </header>
      <h1 class="greeting">Hello Morgan,</h1>
      <div class="body">
        <p>Lorem ipsum dolor sit amet, consectetur adipisicing elit, sed do eiusmod tempor incididunt ut labore et dolore magna aliqua. Ut enim ad minim veniam, quis nostrud exercitation ullamco laboris nisi ut aliquip ex ea commodo consequat.</p>
        <p>Lorem ipsum dolor sit amet, consectetur adipisicing elit, sed do eiusmod tempor incididunt ut labore et dolore magna aliqua. Ut enim ad minim veniam, quis nostrud exercitation ullamco laboris nisi ut aliquip ex ea commodo consequat. Duis aute irure dolor in reprehenderit in voluptate velit esse cillum dolore eu fugiat nulla pariatur. Excepteur sint occaecat cupidatat non proident, sunt in culpa qui officia deserunt mollit anim id est laborum. Sed ut perspiciatis unde omnis iste natus error sit voluptatem accusantium doloremque laudantium.</p>
        <p>Lorem ipsum dolor sit amet, consectetur adipisicing elit, sed do eiusmod tempor incididunt ut labore et dolore magna aliqua. Ut enim ad minim veniam, quis nostrud exercitation ullamco laboris nisi ut aliquip ex ea commodo consequat.</p>
      </div>
    </article>
    <div class="pocket"></div>
    <div class="partners">
      <div class="partner">
        <div class="partner__mark"><span class="partner__dot"></span><span class="partner__name">Velor Tide Shipping LLC</span></div>
        <span class="partner__city">Dubai, UAE</span>
        <span class="partner__web">www.vtduae-example.com</span>
      </div>
      <div class="partner">
        <div class="partner__mark"><span class="partner__dot"></span><span class="partner__name">QMD Shipping Line Ltd</span></div>
        <span class="partner__city">London, UK</span>
        <span class="partner__web">www.qmdfleet-example.com</span>
      </div>
    </div>
  </section>

  <section class="panel panel--right">
    <div class="pocket">
      <div class="slot">
        <div class="card">
          <div class="card__top">
            <div class="brand">
              <span class="brand__dot"></span>
              <p class="brand__name">Borumand Talaj<br>International<br>Transport Co. Ltd</p>
            </div>
            <div class="person">
              <p class="person__name">MS. LEILA DARVISHI</p>
              <p class="person__role">Chief Financial Officer</p>
            </div>
          </div>
          <div class="card__bottom">
            <ul class="contact">
              <li><svg viewBox="0 0 10 10"><path d="M2 1h2l1 2-1 1a6 6 0 0 0 2 2l1-1 2 1v2c0 .6-.4 1-1 1A8 8 0 0 1 1 2c0-.6.4-1 1-1z"/></svg>+98 21 55402913</li>
              <li><svg viewBox="0 0 10 10"><rect x="1" y="3" width="8" height="5"/><rect x="3" y="1" width="4" height="2"/></svg>+98 21 55406287</li>
              <li><svg viewBox="0 0 10 10"><path d="M1 2h8v6H1z"/></svg>info@borumandtalaj-example.com</li>
              <li><svg viewBox="0 0 10 10"><circle cx="5" cy="5" r="4"/></svg>www.borumandtalaj-example.com</li>
            </ul>
            <p class="card__addr">No.8, 2nd Sadaf<br>Kuy-e-Nilufari, Tehran, IR</p>
          </div>
        </div>
        <span class="slot__cut slot__cut--l"></span>
        <span class="slot__cut slot__cut--r"></span>
      </div>
    </div>
  </section>
</main>
</body>
</html>
```